New Business Card

We need to refresh our business cards. We designed these ourselves and we have no graphic design experience. We would like to find a new business card design that is professional and unique. We are an auto finance company. Feel free to play with the logo, but we would like to keep the eye very present on the card. Our corporate colors are green, grey, and white.
Green - RGB - 168,215,27; HEX - #AADD22
Grey - RGB - 196,196,196; HEX - #C4C4C4
Updates
Need to upload the vector file to finalize the project. The last logo was for a jpeg that didn't stretch well.
Industry/Entity Type
Financial Service
Contact Information for Business Card
Honestly don't know...I need your help!

```html
<!DOCTYPE html>
<html lang="en">
<head>
<meta charset="utf-8">
<title>Brightlane Capital – Business Card</title>
<link href="https://fonts.googleapis.com/css2?family=Arimo:wght@400;700&family=Open+Sans:wght@600&display=swap" rel="stylesheet">
<style>
  :root {
    --backdrop: #c4c2c3;
    --green: #aadd22;
    --grey: #c4c4c4;
    --white: #ffffff;
    --black: #0b0b0b;
    --ink: #111111;
    --silver: #b8b8b8;
  }
  html, body {
    margin: 0;
    width: 1200px;
    height: 1000px;
    overflow: hidden;
    background: var(--backdrop);
  }
  .stage {
    width: 1200px;
    height: 1000px;
    display: flex;
    align-items: center;
    justify-content: center;
    gap: 40px;
  }
  .card {
    position: relative;
    width: 520px;
    height: 300px;
    border-radius: 22px;
    overflow: hidden;
  }
  .card--back {
    background: var(--black);
    display: flex;
    align-items: center;
    justify-content: center;
  }
  .card--back .wordmark {
    font-family: "Open Sans", sans-serif;
    font-weight: 600;
    font-size: 34px;
    color: var(--silver);
    letter-spacing: 0.5px;
  }
  .card--front { background: var(--white); }
  .card__shapes {
    position: absolute;
    inset: 0;
    width: 100%;
    height: 100%;
  }
  .brand {
    position: absolute;
    left: 34px;
    top: 110px;
    font-family: "Open Sans", sans-serif;
    font-weight: 600;
    font-size: 28px;
    line-height: 1.1;
    color: var(--green);
  }
  .person {
    position: absolute;
    right: 22px;
    top: 96px;
    text-align: right;
    font-family: "Arimo", sans-serif;
    color: var(--ink);
  }
  .person__name { font-weight: 700; font-size: 20px; letter-spacing: 0.5px; }
  .person__role { font-size: 15px; margin-top: 1px; }
  .contact {
    position: absolute;
    display: flex;
    align-items: center;
    gap: 12px;
    font-family: "Arimo", sans-serif;
    font-size: 14px;
    color: var(--ink);
  }
  .contact__icon {
    width: 26px;
    height: 26px;
    flex: none;
  }
  .contact--phone { left: 236px; top: 200px; }
  .contact--email { left: 210px; top: 225px; }
  .contact--web { left: 183px; top: 250px; }
</style>
</head>
<body>
<main class="stage">
  <section class="card card--back" aria-label="Card back">
    <span class="wordmark">Brightlane Capital</span>
  </section>

  <section class="card card--front" aria-label="Card front">
    <svg class="card__shapes" viewBox="0 0 520 300" aria-hidden="true">
      <polygon points="330,0 455,0 330,119" fill="var(--black)"/>
      <polygon points="140,300 455,0 490,0 180,300" fill="var(--grey)"/>
      <polygon points="180,300 490,0 520,0 520,300" fill="var(--green)"/>
    </svg>

    <div class="brand">Brightlane<br>Capital</div>

    <div class="person">
      <div class="person__name">JOHN DOE</div>
      <div class="person__role">Manager</div>
    </div>

    <div class="contact contact--phone">
      <svg class="contact__icon" viewBox="0 0 26 26" aria-hidden="true">
        <circle cx="13" cy="13" r="11.5" fill="var(--green)" stroke="var(--ink)" stroke-width="2"/>
        <path d="M9.5 7.5l2.2-.5 1.2 3-1.4 1c.6 1.4 1.6 2.4 3 3l1-1.4 3 1.2-.5 2.2c-4.5.3-8.8-4-8.5-8.5z" fill="var(--ink)"/>
      </svg>
      <span>012.345.6789</span>
    </div>
    <div class="contact contact--email">
      <svg class="contact__icon" viewBox="0 0 26 26" aria-hidden="true">
        <circle cx="13" cy="13" r="11.5" fill="var(--green)" stroke="var(--ink)" stroke-width="2"/>
        <rect x="7" y="9" width="12" height="8.5" fill="var(--ink)"/>
        <path d="M7 9l6 5 6-5" fill="none" stroke="var(--green)" stroke-width="1.2"/>
      </svg>
      <span>email@brightlane.com</span>
    </div>
    <div class="contact contact--web">
      <svg class="contact__icon" viewBox="0 0 26 26" aria-hidden="true">
        <circle cx="13" cy="13" r="11.5" fill="var(--green)" stroke="var(--ink)" stroke-width="2"/>
        <g fill="none" stroke="var(--ink)" stroke-width="1.3">
          <circle cx="13" cy="13" r="6"/>
          <ellipse cx="13" cy="13" rx="2.6" ry="6"/>
          <line x1="7" y1="13" x2="19" y2="13"/>
        </g>
      </svg>
      <span>www.brightlane.com</span>
    </div>
  </section>
</main>
</body>
</html>
```